Business Card Design for Engineering Firm

Need a business card design for small mechanical and plumbing engineering form based in Utah. Design should be customizable for all employees.

```html
<!DOCTYPE html>
<html lang="en">
<head>
<meta charset="utf-8">
<title>Larkspur Engineering – Business Card</title>
<link rel="stylesheet" href="https://fonts.googleapis.com/css2?family=Montserrat:wght@600;700&family=Open+Sans:wght@400;600&display=swap">
<style>
  :root {
    --stage: #232324;
    --card: #1e1e21;
    --edge-red: #8e1b1d;
    --brand-red: #8b1e1f;
    --emboss: #0f0f11;
    --ink-light: #ffffff;
    --ink-muted: #d9d9dc;
  }
  * { box-sizing: border-box; margin: 0; padding: 0; }
  html, body {
    width: 1200px; height: 780px; overflow: hidden;
    background: var(--stage);
  }
  .canvas {
    position: relative; width: 1200px; height: 780px;
  }
  .card {
    position: absolute; top: 236px;
    width: 540px; height: 309px;
    background: var(--card);
    border-radius: 18px;
    border-bottom: 4px solid var(--edge-red);
    overflow: hidden;
  }
  .card--back { left: 40px; }
  .card--front { left: 620px; }

  /* Back */
  .back-mark {
    position: absolute; inset: 0;
    display: flex; align-items: center; justify-content: center; gap: 16px;
  }
  .back-mark__square {
    width: 34px; height: 34px; background: var(--emboss);
  }
  .back-mark__name {
    font-family: "Montserrat", sans-serif; font-weight: 700;
    font-size: 28px; letter-spacing: 1px; color: var(--emboss);
    text-transform: uppercase; line-height: 1.1;
  }

  /* Front */
  .accent-tab {
    position: absolute; right: 14px; top: 22px;
    width: 16px; height: 62px; background: var(--brand-red);
  }
  .person {
    position: absolute; right: 40px; top: 26px; text-align: right;
    font-family: "Montserrat", sans-serif;
  }
  .person__name { font-size: 26px; font-weight: 700; line-height: 1.1; }
  .person__first { color: var(--brand-red); }
  .person__last { color: var(--ink-light); }
  .person__title {
    font-family: "Open Sans", sans-serif; font-weight: 400;
    font-size: 13px; color: var(--ink-light); margin-top: 3px; letter-spacing: .3px;
  }
  .brand {
    position: absolute; left: 38px; top: 118px;
    display: flex; align-items: center; gap: 12px;
  }
  .brand__square { width: 22px; height: 22px; background: var(--brand-red); }
  .brand__name {
    font-family: "Montserrat", sans-serif; font-weight: 700;
    font-size: 19px; letter-spacing: .5px; color: var(--brand-red);
    text-transform: uppercase; line-height: 1.15;
  }
  .contact {
    position: absolute; left: 38px; bottom: 26px;
    font-family: "Open Sans", sans-serif; font-size: 13px;
    color: var(--ink-light); line-height: 1.45;
  }
  .contact__address { margin-bottom: 8px; }
  .contact__list { list-style: none; }
  .contact__item { display: flex; align-items: center; gap: 8px; }
  .contact__icon { width: 12px; height: 12px; flex: none; }
</style>
</head>
<body>
<main class="canvas">

  <section class="card card--back" aria-label="Card back">
    <div class="back-mark">
      <span class="back-mark__square"></span>
      <span class="back-mark__name">Larkspur<br>Engineering</span>
    </div>
  </section>

  <section class="card card--front" aria-label="Card front">
    <span class="accent-tab"></span>

    <div class="person">
      <p class="person__name"><span class="person__first">Mirela</span> <span class="person__last">Hostova</span></p>
      <p class="person__title">Managing Director</p>
    </div>

    <div class="brand">
      <span class="brand__square"></span>
      <span class="brand__name">Larkspur<br>Engineering</span>
    </div>

    <div class="contact">
      <p class="contact__address">1840 Canyon Ridge Rd. Suite 300<br>Provo, UT 84604</p>
      <ul class="contact__list">
        <li class="contact__item">
          <svg class="contact__icon" viewBox="0 0 24 24" aria-hidden="true"><path fill="#8b1e1f" d="M6.6 10.8a15.1 15.1 0 0 0 6.6 6.6l2.2-2.2c.3-.3.7-.4 1-.2 1.1.4 2.3.6 3.6.6.6 0 1 .4 1 1V20c0 .6-.4 1-1 1A17 17 0 0 1 3 4c0-.6.4-1 1-1h3.5c.6 0 1 .4 1 1 0 1.3.2 2.5.6 3.6.1.3 0 .7-.2 1z"/></svg>
          (801) 555-0147
        </li>
        <li class="contact__item">
          <svg class="contact__icon" viewBox="0 0 24 24" aria-hidden="true"><rect x="2" y="5" width="20" height="14" rx="2" fill="#8b1e1f"/><path d="M3 6l9 7 9-7" fill="none" stroke="#1e1e21" stroke-width="2"/></svg>
          info@larkspureng.com
        </li>
        <li class="contact__item">
          <svg class="contact__icon" viewBox="0 0 24 24" aria-hidden="true"><circle cx="12" cy="12" r="10" fill="#8b1e1f"/><path d="M2 12h20M12 2c3 3 3 17 0 20M12 2c-3 3-3 17 0 20" fill="none" stroke="#1e1e21" stroke-width="1.5"/></svg>
          www.larkspureng.com
        </li>
      </ul>
    </div>
  </section>

</main>
</body>
</html>
```